BRL business card

For a business card with our logo

Contact Information for Business Card

Mathéo VRANEL
Founder & CEO
email : ceo@brightlanterncollective.com / www.brightlanterncollective.com /
instagram / facebook / WhatsApp
N°: +590 690 482 517

Colors

Designer to choose colors to be used in the design.

```html
<!DOCTYPE html>
<html lang="en">
<head>
<meta charset="UTF-8">
<title>BRL Business Card</title>
<link rel="stylesheet" href="https://fonts.googleapis.com/css2?family=Roboto:wght@400;700&display=swap">
<style>
  :root {
    --backdrop: #2b2b2d;
    --card: #141416;
    --orange: #f07325;
    --blue: #1557b0;
    --white: #f4f4f4;
  }
  * { margin: 0; padding: 0; box-sizing: border-box; }
  html, body {
    width: 1200px;
    height: 900px;
    overflow: hidden;
    background: var(--backdrop);
    font-family: "Roboto", sans-serif;
  }
  .canvas { position: relative; width: 1200px; height: 900px; }

  .card {
    position: absolute;
    width: 700px;
    height: 400px;
    background: var(--card);
    overflow: hidden;
    box-shadow: 0 12px 30px rgba(0,0,0,.45);
  }
  .card--front { left: 400px; top: 30px; }
  .card--back { left: 100px; top: 470px; }

  .brand {
    position: absolute;
    display: flex;
    flex-direction: column;
    align-items: center;
    gap: 14px;
  }
  .card--front .brand { left: 0; right: 0; top: 110px; }
  .card--back .brand { left: 30px; width: 300px; top: 95px; }

  .brand-mark {
    width: 96px;
    height: 96px;
    border-radius: 50%;
    background: var(--orange);
  }
  .brand-name {
    font-weight: 700;
    font-size: 22px;
    letter-spacing: 1.5px;
    color: var(--blue);
    text-align: center;
    line-height: 1.2;
  }

  .divider {
    position: absolute;
    left: 350px;
    top: 80px;
    width: 2px;
    height: 220px;
    background: var(--blue);
  }

  .contact {
    position: absolute;
    left: 385px;
    top: 78px;
    color: var(--white);
  }
  .contact-name {
    font-weight: 700;
    font-size: 27px;
    color: var(--orange);
    letter-spacing: .5px;
  }
  .contact-role {
    font-size: 18px;
    margin: 4px 0 16px;
  }
  .contact-list { list-style: none; }
  .contact-item {
    display: flex;
    align-items: center;
    gap: 10px;
    font-size: 16px;
    margin-bottom: 10px;
  }
  .contact-icon { width: 16px; height: 16px; flex: none; }
  .social-dot {
    width: 14px;
    height: 14px;
    border-radius: 50%;
    background: var(--orange);
    flex: none;
    margin-left: 1px;
  }

  .wave { position: absolute; left: 0; top: 0; width: 700px; height: 400px; }
</style>
</head>
<body>
<div class="canvas">

  <section class="card card--front">
    <div class="brand">
      <div class="brand-mark"></div>
      <div class="brand-name">BRIGHT LANTERN<br>COLLECTIVE</div>
    </div>
  </section>

  <section class="card card--back">
    <svg class="wave" viewBox="0 0 700 400" aria-hidden="true">
      <path d="M0 255 C 180 330, 420 395, 700 372 L700 400 L0 400 Z" fill="var(--orange)"/>
      <path d="M300 338 C 470 378, 600 372, 700 352 L700 368 C 590 386, 460 384, 300 338 Z" fill="#0d0d0f"/>
      <path d="M300 338 C 470 372, 600 366, 700 348 L700 360 C 590 380, 460 378, 300 338 Z" fill="var(--blue)"/>
    </svg>

    <div class="brand">
      <div class="brand-mark"></div>
      <div class="brand-name">BRIGHT LANTERN<br>COLLECTIVE</div>
    </div>

    <div class="divider"></div>

    <div class="contact">
      <h1 class="contact-name">MATHÉO VRANEL</h1>
      <p class="contact-role">Founder &amp; CEO</p>
      <ul class="contact-list">
        <li class="contact-item">
          <svg class="contact-icon" viewBox="0 0 16 16"><circle cx="8" cy="8" r="8" fill="var(--orange)"/><path d="M5 4.5l1.6-.4.8 2-1 .8a5 5 0 0 0 2.7 2.7l.8-1 2 .8-.4 1.6c-3.6.2-6.7-2.9-6.5-6.5z" fill="var(--card)"/></svg>
          +590 690 482 517
        </li>
        <li class="contact-item">
          <svg class="contact-icon" viewBox="0 0 16 16"><rect x="1" y="3" width="14" height="10" rx="1" fill="var(--orange)"/><path d="M2 4.5l6 4.5 6-4.5" fill="none" stroke="var(--card)" stroke-width="1.4"/></svg>
          ceo@brightlanterncollective.com
        </li>
        <li class="contact-item">
          <svg class="contact-icon" viewBox="0 0 16 16"><circle cx="8" cy="8" r="7.5" fill="var(--orange)"/><g fill="none" stroke="var(--card)" stroke-width="1"><ellipse cx="8" cy="8" rx="3" ry="7"/><path d="M1 8h14M2.5 4.5h11M2.5 11.5h11"/></g></svg>
          www.brightlanterncollective.com
        </li>
        <li class="contact-item">
          <span class="social-dot"></span>
          @brightlanterncollective
        </li>
      </ul>
    </div>
  </section>

</div>
</body>
</html>
```